Empower our Electric Journey on the Web

We need a new website that can promote our services. Our three services that we offer are:
- Management of e-mobility charging stations
- Management of energy purchases
- Leasing of E-Mobility charging stations
- Energy billing of private electricity meters
The website should work responsively on PC, tablet and smartphone. In general, a simple navigation and an appealing design should be in the foreground. The website should give the customer the possibility to request , based pm a preset chexkbox chart and to get in contact with us.
Our logo works on black and white background.
Our slogan is:
Empower Your Electric Journey with Velnik Mobility
The 4 Pages should be the following:
Main Page, with info about us, why choose us,
2nd; services; what we sell and what are our services
3rd; Contact us, request an offer
4th, References about costumers and Work we already did, in the future we would like to integrate a Blog Post in this section in stead of references.

Target Market(s)

Landlords, Homeowners, Homeowner Associations

Industry/Entity Type

EV Chargers / E-Mobility

Coding

Coded - Design and coding required

Number of Pages Required

4 page

Requirements
Nice to have
• Pop up to our mailchimp newsletter subscription

```html
<!DOCTYPE html>
<html lang="en">
<head>
<meta charset="utf-8">
<title>Velnik Mobility</title>
<link href="https://fonts.googleapis.com/css2?family=Montserrat:wght@400;500;600;700&display=swap" rel="stylesheet">
<style>
:root{
  --green:#3dba3f;
  --green-bright:#7cf77a;
  --green-mid:#5ad35d;
  --ink:#111111;
  --text:#333333;
  --muted:#666666;
  --white:#ffffff;
  --card:rgba(70,70,70,.55);
}
*{margin:0;padding:0;box-sizing:border-box}
html,body{width:1200px;height:4270px;overflow:hidden}
body{font-family:"Montserrat",sans-serif;color:var(--text);background:var(--white);position:relative}
.abs{position:absolute}
.eyebrow{color:var(--green);font-size:16px;letter-spacing:1px;text-transform:uppercase;font-weight:500}
.heading{font-size:36px;font-weight:500;letter-spacing:2.5px;text-transform:uppercase;line-height:1.3;color:var(--ink)}
.btn{background:var(--green);color:var(--white);font-weight:600;font-size:17px;letter-spacing:1px;text-transform:uppercase;display:flex;align-items:center;justify-content:center}
.brand{font-weight:700;font-size:26px;letter-spacing:3px;text-transform:uppercase;display:flex;align-items:center;gap:10px}
.brand-dot{width:18px;height:18px;background:var(--green);border-radius:50%}

/* header */
.site-header{top:0;left:0;width:1200px;height:85px;background:var(--white)}
.site-header .brand{left:145px;top:27px;color:var(--ink);font-size:22px}
.nav{left:432px;top:34px;display:flex;gap:27px;font-size:14px;color:var(--ink)}
.nav .active{position:relative}
.nav .active::after{content:"";position:absolute;left:0;right:0;top:26px;height:3px;background:var(--green)}
.nav-phone{left:783px;top:34px;font-size:14px;color:var(--ink);display:flex;gap:6px;align-items:center}
.nav-cta{left:921px;top:24px;width:135px;height:38px;border:2px solid var(--green);font-size:13px;font-weight:600;letter-spacing:1px;display:flex;align-items:center;justify-content:center;color:var(--ink)}

/* hero */
.hero{top:85px;left:0;width:1200px;height:530px;overflow:hidden;background:var(--ink)}
.hero-photo{position:absolute;left:420px;top:0;width:780px;height:530px;background:radial-gradient(ellipse at 60% 40%,#d9dcda 0%,#8e9491 35%,#2b2f2d 70%,#0e0e0e 100%)}
.hero-cut{position:absolute;left:0;top:0}
.hero h1{position:absolute;left:145px;top:127px;color:var(--white);font-size:37px;font-weight:600;letter-spacing:3px;line-height:1.4;text-transform:uppercase}
.hero h1 span{color:var(--green)}
.hero .sub{position:absolute;left:145px;top:296px;color:var(--white);font-size:17px}
.hero .btn{position:absolute;left:145px;top:353px;width:175px;height:50px}

/* about */
.about-photo{left:0;top:672px;width:613px;height:548px;background:linear-gradient(120deg,#5b5f60 0%,#9ea5a3 40%,#3a3d3f 100%)}
.about-stripes{left:540px;top:1040px}
.about-copy{left:657px;top:706px;width:400px}
.about-copy .heading{margin-top:8px;font-size:35px}
.about-copy .intro{font-size:13px;line-height:1.65;margin-top:14px;color:var(--text)}
.feature{margin-top:22px}
.feature h4{font-size:17px;font-weight:500;letter-spacing:1px;display:flex;align-items:center;gap:12px;color:var(--ink)}
.feature p{font-size:12.5px;line-height:1.65;margin-top:8px;color:var(--muted)}

/* services */
.services{top:1220px;left:0;width:1200px;height:992px;background:linear-gradient(120deg,#161616 0%,#222 45%,#3d3f3f 75%,#2a2a2a 100%)}
.services .eyebrow{position:absolute;left:0;width:1200px;text-align:center;top:93px}
.services .heading{position:absolute;left:0;width:1200px;text-align:center;top:120px;color:var(--white)}
.card{position:absolute;width:444px;height:335px;border:1.5px solid var(--green);background:var(--card);padding:30px 52px;color:var(--white)}
.card h3{font-size:16px;font-weight:600;letter-spacing:1.2px;line-height:1.45;text-transform:uppercase;margin-top:20px}
.card p{font-size:13px;line-height:1.65;margin-top:18px;color:#e4e4e4}
.card b{font-weight:700;color:var(--white)}
.card .more{position:absolute;left:52px;bottom:35px;color:var(--green);font-size:17px;letter-spacing:1px;text-transform:uppercase;display:flex;align-items:center;gap:10px}

/* why */
.why-photo{left:666px;top:2212px;width:534px;height:607px;background:linear-gradient(150deg,#8fe09a 0%,#3fae55 40%,#1f7a3a 75%,#4fc469 100%)}
.why-copy{left:143px;top:2315px;width:430px}
.why-copy .heading{margin-top:10px;font-size:36px}
.reason{display:flex;gap:18px;margin-top:40px}
.reason .ring{flex:0 0 58px;height:58px;border:1px solid #ccc;border-radius:50%;display:flex;align-items:center;justify-content:center}
.reason h4{font-size:17px;font-weight:600;color:var(--ink);letter-spacing:.5px}
.reason p{font-size:12.5px;line-height:1.7;margin-top:10px;color:var(--muted)}
.reason b{color:var(--text)}

/* cta */
.cta{top:2819px;left:0;width:1200px;height:374px;background:linear-gradient(100deg,#1d5a20 0%,#143716 35%,#0f1f10 70%,#0a120a 100%);overflow:hidden}
.cta .eyebrow{position:absolute;left:0;width:1200px;text-align:center;top:88px;color:var(--white)}
.cta .heading{position:absolute;left:0;width:1200px;text-align:center;top:117px;color:var(--white);font-size:37px}
.cta .btn{position:absolute;left:480px;top:270px;width:240px;height:48px}

/* testimonials */
.reviews .eyebrow{position:absolute;left:0;width:1200px;text-align:center;top:3280px}
.reviews .heading{position:absolute;left:0;width:1200px;text-align:center;top:3307px}
.quote{position:absolute;top:3390px;width:290px}
.stars{color:var(--green);font-size:21px;letter-spacing:3px}
.quote p{font-size:12.5px;line-height:1.7;margin-top:8px;color:var(--text)}
.quote .who{margin-top:22px;font-size:15px;font-weight:600;color:var(--ink)}
.quote .role{font-size:9px;color:var(--muted);margin:4px 0 0 18px}
.dots{left:574px;top:3624px;display:flex;gap:12px}
.dots span{width:10px;height:10px;border:1px solid #bbb}
.dots span.on{background:var(--green);border-color:var(--green)}

/* newsletter + footer */
.footer{top:3650px;left:0;width:1200px;height:620px;background:var(--ink);color:var(--white)}
.footer .green-band{position:absolute;left:0;top:-12px}
.news-title{left:143px;top:100px;font-size:36px;font-weight:500;letter-spacing:3px}
.news-text{left:143px;top:164px;font-size:13px;line-height:1.65;width:440px}
.news-form{left:615px;top:147px;width:441px;height:51px;border:1px solid var(--green);display:flex}
.news-form .field{flex:1;display:flex;align-items:center;padding-left:22px;font-size:13px;color:#ccc}
.news-form .btn{width:137px;font-size:14px;margin:3px}
.rule{left:143px;top:233px;width:913px;height:1px;background:#555}
.footer .brand{left:143px;top:298px;color:var(--white);font-size:24px}
.socials{left:207px;top:371px;display:flex;gap:8px}
.socials span{width:22px;height:22px;border:1px solid #aaa;border-radius:50%}
.fcol{top:282px;font-size:13px;line-height:1.35}
.fcol h5{font-size:13px;font-weight:600;letter-spacing:1px;text-transform:uppercase;border-left:2px solid var(--white);padding-left:12px;margin-left:-14px;margin-bottom:26px}
.fcol li{list-style:none;margin-bottom:15px}
.info{display:flex;gap:12px;color:#bbb;margin-bottom:22px}
.bottom-bar{left:0;top:567px;width:1200px;height:53px;background:#2a2a2a;display:flex;justify-content:space-between;align-items:center;padding:0 143px;font-size:13px}
</style>
</head>
<body>

<header class="abs site-header">
  <div class="abs brand"><span class="brand-dot"></span>Velnik Mobility</div>
  <nav class="abs nav"><span class="active">Home</span><span>About Us</span><span>Services</span><span>Our Partners</span></nav>
  <div class="abs nav-phone">
    <svg width="12" height="12" viewBox="0 0 24 24"><path fill="#3dba3f" d="M6.6 10.8a15 15 0 006.6 6.6l2.2-2.2c.3-.3.7-.4 1-.2 1.1.4 2.300.6 3.6.6.6 0 1 .4 1 1V20c0 .6-.4 1-1 1A17 17 0 013 4c0-.6.4-1 1-1h3.5c.6 0 1 .4 1 1 0 1.3.2 2.5.6 3.6.1.3 0 .7-.2 1z"/></svg>
    (555) 014-2270</div>
  <div class="abs nav-cta">CONTACT US</div>
</header>

<section class="abs hero">
  <div class="hero-photo" role="img" aria-label="Electric vehicle plugged into a glowing wall charger"></div>
  <svg class="hero-cut" width="1200" height="530" viewBox="0 0 1200 530">
    <defs><linearGradient id="hg" x1="0" x2="1"><stop offset="0" stop-color="#111" stop-opacity="1"/><stop offset=".55" stop-color="#111" stop-opacity=".85"/><stop offset="1" stop-color="#111" stop-opacity="0"/></linearGradient></defs>
    <rect x="420" y="0" width="400" height="530" fill="url(#hg)"/>
    <polygon points="0,445 700,530 0,530" fill="#fff"/>
    <polygon points="700,530 1200,410 1200,530" fill="#7cf77a"/>
    <polygon points="1050,530 1200,490 1200,530" fill="#3dba3f"/>
  </svg>
  <h1>Empower Your<br>Electric Journey<br>With <span>Velnik Mobility</span></h1>
  <p class="sub">Your Partner In E-Mobility Solutions</p>
  <div class="btn">Get Started</div>
</section>

<div class="abs about-photo" role="img" aria-label="Business consultant holding a charging plug beside a branded wall charger"></div>
<svg class="abs about-stripes" width="145" height="180" viewBox="0 0 145 180">
  <polygon points="7,0 32,0 48,50 23,50" fill="#7cf77a"/>
  <polygon points="32,56 60,56 90,120 62,120" fill="#5ad35d"/>
  <polygon points="32,133 100,133 140,180 72,180" fill="#3dba3f"/>
</svg>
<div class="abs about-copy">
  <div class="eyebrow">Who We Are</div>
  <h2 class="heading">Velnik Mobility</h2>
  <p class="intro"><b>Velnik Mobility</b> is your trusted partner in the world of electric mobility. With a strong commitment to sustainability and innovation, we offer a comprehensive range of services designed to streamline and enhance your electric journey.</p>
  <div class="feature"><h4><svg width="22" height="22" viewBox="0 0 24 24"><circle cx="12" cy="12" r="10" fill="none" stroke="#3dba3f" stroke-width="2"/><path d="M7 12l3.5 3.5L17 9" fill="none" stroke="#3dba3f" stroke-width="2"/></svg>Efficient Cost Savings</h4><p>Optimize electricity usage, reducing operational costs.</p></div>
  <div class="feature"><h4><svg width="22" height="22" viewBox="0 0 24 24"><circle cx="12" cy="12" r="10" fill="none" stroke="#3dba3f" stroke-width="2"/><path d="M7 12l3.5 3.5L17 9" fill="none" stroke="#3dba3f" stroke-width="2"/></svg>User-Friendly Access</h4><p>Enhance user experience with easy station access.</p></div>
  <div class="feature"><h4><svg width="22" height="22" viewBox="0 0 24 24"><circle cx="12" cy="12" r="10" fill="none" stroke="#3dba3f" stroke-width="2"/><path d="M7 12l3.5 3.5L17 9" fill="none" stroke="#3dba3f" stroke-width="2"/></svg>Environmental Responsibility</h4><p>Promote sustainability by using clean energy and<br>efficient scheduling.</p></div>
</div>

<section class="abs services">
  <div class="eyebrow">What We Do</div>
  <h2 class="heading">Our Services</h2>
  <article class="card" style="left:143px;top:205px">
    <svg width="40" height="42" viewBox="0 0 40 42" fill="none" stroke="#fff" stroke-width="1.8"><rect x="6" y="3" width="18" height="36" rx="2"/><rect x="10" y="8" width="10" height="10"/><path d="M24 14h6v16a3 3 0 006 0V10M33 4v6M37 4v6"/></svg>
    <h3>Management of E-Mobility Charging Stations</h3>
    <p>Ensure seamless operation and maintenance of your charging stations with our expert management services. We handle everything from installation to <b>24/7 monitoring</b>, ensuring a hassle-free experience for your customers.</p>
    <div class="more">Learn More <svg width="34" height="10" viewBox="0 0 34 10"><path d="M0 5h32M27 1l5 4-5 4" stroke="#3dba3f" fill="none" stroke-width="1.5"/></svg></div>
  </article>
  <article class="card" style="left:612px;top:205px">
    <svg width="44" height="42" viewBox="0 0 44 42" fill="none" stroke="#fff" stroke-width="1.8"><circle cx="22" cy="21" r="9"/><path d="M22 15v12M25 17h-4a2 2 0 000 4h2a2 2 0 010 4h-4"/><path d="M8 21a14 14 0 0124-10M36 21a14 14 0 01-24 10M32 5v6h-6M12 37v-6h6"/></svg>
    <h3>Management of Energy<br>Purchases</h3>
    <p>Optimize your energy procurement with <b>Velnik Mobility</b>. Our energy experts will help you make informed decisions, saving you money while reducing your carbon footprint.</p>
    <div class="more">Learn More <svg width="34" height="10" viewBox="0 0 34 10"><path d="M0 5h32M27 1l5 4-5 4" stroke="#3dba3f" fill="none" stroke-width="1.5"/></svg></div>
  </article>
  <article class="card" style="left:143px;top:565px">
    <svg width="54" height="42" viewBox="0 0 54 42" fill="none" stroke="#fff" stroke-width="1.8"><circle cx="30" cy="14" r="10" stroke="#3dba3f"/><path d="M30 8v12M33 10h-4a2 2 0 000 4h2a2 2 0 010 4h-4" stroke="#3dba3f"/><path d="M2 30h10l8 4h12a3 3 0 000-6H22M12 30l10-4h8M2 38h10l10 3 28-10"/></svg>
    <h3>Leasing of E-Mobility Charging Stations</h3>
    <p>Explore the benefits of our charging station <b>leasing program</b>. We provide cost-effective solutions, allowing you to offer charging services without the upfront investment.</p>
    <div class="more">Learn More <svg width="34" height="10" viewBox="0 0 34 10"><path d="M0 5h32M27 1l5 4-5 4" stroke="#3dba3f" fill="none" stroke-width="1.5"/></svg></div>
  </article>
  <article class="card" style="left:612px;top:565px">
    <svg width="40" height="42" viewBox="0 0 40 42" fill="none" stroke="#fff" stroke-width="1.8"><rect x="4" y="4" width="32" height="30" rx="3"/><rect x="9" y="9" width="22" height="7"/><path d="M21 19l-3 5h4l-3 5" stroke="#3dba3f"/><path d="M10 34v4M20 34v4M30 34v4"/></svg>
    <h3>Energy Billing of Private<br>Electricity Meters</h3>
    <p>Simplify the billing process for <b>private electricity meters</b> within your properties. Our efficient energy billing services ensure accurate and transparent transactions.</p>
    <div class="more">Learn More <svg width="34" height="10" viewBox="0 0 34 10"><path d="M0 5h32M27 1l5 4-5 4" stroke="#3dba3f" fill="none" stroke-width="1.5"/></svg></div>
  </article>
</section>

<div class="abs why-photo" role="img" aria-label="Row of green EV charging stations with plugged-in cables"></div>
<div class="abs why-copy">
  <div class="eyebrow">Features</div>
  <h2 class="heading">Why Choose<br>Velnik Mobility</h2>
  <div class="reason">
    <div class="ring"><svg width="32" height="32" viewBox="0 0 32 32" fill="none" stroke="#3dba3f" stroke-width="1.5"><circle cx="16" cy="8" r="3"/><path d="M11 16a5 5 0 0110 0"/><path d="M16 18l2 4 4 .5-3 3 .8 4.5-3.8-2-3.8 2 .8-4.5-3-3 4-.5z"/></svg></div>
    <div><h4>Expertise</h4><p>Our team of seasoned professionals brings extensive knowledge of the <b>EV charging</b> and <b>energy management industry</b>, ensuring top-notch solutions for your needs.</p></div>
  </div>
  <div class="reason">
    <div class="ring"><svg width="32" height="32" viewBox="0 0 32 32" fill="none" stroke="#3dba3f" stroke-width="1.5"><path d="M16 22V10M16 16c-4 0-6-3-6-7 4 0 6 3 6 7zM16 13c0-4 2-7 7-7 0 4-3 7-7 7z"/><path d="M4 24h6l5 2h6a2 2 0 000-4h-5M4 29h7l6 1 11-5"/></svg></div>
    <div><h4>Sustainability</h4><p>At <b>Velnik Mobility</b>, sustainability is at the core of what we do. We're dedicated to helping you reduce your carbon footprint while embracing the electric future.</p></div>
  </div>
</div>

<section class="abs cta">
  <div class="eyebrow">Simplifying Sustainability</div>
  <h2 class="heading">Ready to Empower Your<br>Electric Journey?</h2>
  <div class="btn">Request an Offer</div>
</section>

<section class="reviews">
  <div class="eyebrow">What We Do</div>
  <h2 class="heading">What Our Clients Say</h2>
  <div class="quote" style="left:143px"><div class="stars">★★★★★</div><p>"Velnik Mobility has transformed our property into a sustainable and forward-thinking community. Their charging station management has been exceptional."</p><div class="who">— Tomas Reyle</div><div class="role">Homeowner Association President</div></div>
  <div class="quote" style="left:470px"><div class="stars">★★★★★</div><p>"We've seen significant cost savings and improved energy efficiency since partnering with Velnik Mobility for energy procurement. Highly recommended!"</p><div class="who">— Mira Caldwell</div><div class="role">Landlord</div></div>
  <div class="quote" style="left:768px"><div class="stars">★★★★★</div><p>"The leasing program offered by Velnik Mobility was a game-changer for our business. It allowed us to offer EV charging without the financial burden. Great service!"</p><div class="who">— Owen Farrow</div><div class="role">Business Owner</div></div>
  <div class="abs dots"><span class="on"></span><span></span><span></span></div>
</section>

<footer class="abs footer">
  <svg class="green-band" width="1200" height="100" viewBox="0 0 1200 100"><polygon points="620,75 1200,0 1200,65" fill="#7cf77a"/></svg>
  <h2 class="abs news-title">STAY INFORMED</h2>
  <p class="abs news-text">Sign up for our newsletter to receive the latest updates on electric mobility trends, industry insights, and exclusive offers.</p>
  <div class="abs news-form"><div class="field">Your Email...</div><div class="btn">Subscribe</div></div>
  <div class="abs rule"></div>
  <div class="abs brand"><span class="brand-dot"></span>Velnik Mobility</div>
  <div class="abs socials"><span></span><span></span><span></span></div>
  <div class="abs fcol" style="left:461px"><h5>Quick Link</h5><ul><li>Home</li><li>About Us</li><li>Services</li><li>Our Partners</li><li>Competed Work</li><li>Contact Us</li></ul></div>
  <div class="abs fcol" style="left:652px;width:170px"><h5>Services</h5><ul><li>Management of E-Mobility Charging Stations</li><li>Management of Energy Purchases</li><li>Leasing of E-Mobility Charging Stations</li><li>Energy Billing Of Private Electricity Meters</li></ul></div>
  <div class="abs fcol" style="left:868px;width:200px"><h5>Contact Info</h5>
    <div class="info"><svg width="14" height="18" viewBox="0 0 24 30"><path fill="#3dba3f" d="M12 0a10 10 0 00-10 10c0 8 10 20 10 20s10-12 10-20A10 10 0 0012 0zm0 14a4 4 0 110-8 4 4 0 010 8z"/></svg><span>48 Birchline Avenue<br>Oakhaven, CA 90417<br>United States</span></div>
    <div class="info"><svg width="15" height="15" viewBox="0 0 24 24"><path fill="#3dba3f" d="M6.6 10.8a15 15 0 006.6 6.6l2.2-2.2c.3-.3.7-.4 1-.2 1.1.4 2.3.6 3.6.6.6 0 1 .4 1 1V20c0 .6-.4 1-1 1A17 17 0 013 4c0-.6.4-1 1-1h3.5c.6 0 1 .4 1 1 0 1.3.2 2.5.6 3.6.1.3 0 .7-.2 1z"/></svg><span>(555) 014-2270</span></div>
    <div class="info"><svg width="15" height="12" viewBox="0 0 24 18"><rect width="24" height="18" fill="#3dba3f"/><path d="M0 0l12 9 12-9" stroke="#111" fill="none" stroke-width="2"/></svg><span>hello@velnikmobility.com</span></div>
  </div>
  <div class="abs bottom-bar"><span>© 2023 All Rights Reserved | Velnik Mobility</span><span>Privacy Policy | Terms and Conditions</span></div>
</footer>

</body>
</html>
```